National hospice pharmacy network is needing a flier

We need an informational flier for a new company that is creating a network of independent pharmacies to provide medication delivery to hospice patients in their area. We will be providing them with logistics to build a delivery system, software to increase efficiency and the marketing to hospice agencies. The pharmacies will benefit with increasing their patient care, increasing their efficiency and increasing their profits.

It needs to be scalable from postcard to full size (8.5 x 11)
Logo style final but colors are being darkened. Will provide final logo when finalized.

Industry/Entity Type

Marketing

```html
<!DOCTYPE html>
<html lang="en">
<head>
<meta charset="utf-8">
<title>Hearthway – Local Pharmacy Network Flier</title>
<link rel="stylesheet" href="https://fonts.googleapis.com/css2?family=Lato:ital,wght@0,400;0,700;0,900;1,700&family=Pathway+Gothic+One&display=swap">
<style>
  :root{
    --brand-blue:#2a5ea8;
    --navy:#0d2f78;
    --navy-deep:#08235c;
    --cell-blue:#3a72c2;
    --green:#2fbf3c;
    --green-dark:#23a52f;
    --green-title:#2fb341;
    --ink:#333a40;
    --paper-top:#ffffff;
    --paper-bottom:#e9eaec;
  }
  *{box-sizing:border-box;margin:0;padding:0}
  html,body{width:932px;height:1200px;overflow:hidden}
  body{background:#dcdcdc;font-family:"Lato",Arial,sans-serif}
  .flier{
    position:relative;width:932px;height:1200px;overflow:hidden;
    background:linear-gradient(180deg,var(--paper-top) 0%,#f4f4f5 55%,var(--paper-bottom) 100%);
  }
  .hero-photo{
    position:absolute;inset:0 0 auto 0;height:443px;
    clip-path:polygon(487px 0,932px 0,932px 443px,150px 443px);
    background:
      radial-gradient(ellipse 210px 260px at 760px 250px,#f7f5f1 0%,rgba(247,245,241,0) 70%),
      linear-gradient(90deg,#c9d3df 0%,#e3e6ea 35%,#d6dbe2 60%,#eef0f2 100%);
  }
  .hero-edge{position:absolute;left:0;top:0;width:932px;height:460px;pointer-events:none}
  .brand{
    position:absolute;left:32px;top:42px;display:flex;align-items:center;gap:12px;
    font-family:"Lato",Arial,sans-serif;font-weight:400;font-size:78px;line-height:1;letter-spacing:-1.5px;color:var(--brand-blue);
  }
  .brand-dot{width:22px;height:22px;border-radius:50%;background:var(--green);margin-top:24px}
  .question{
    position:absolute;left:0;height:61px;padding:0 60px 0 35px;
    display:flex;align-items:center;
    background:linear-gradient(180deg,#3cd045 0%,var(--green-dark) 100%);
    color:#fff;font-weight:700;font-style:italic;font-size:19px;line-height:1.3;white-space:nowrap;
  }
  .q1{top:198px;width:617px;clip-path:polygon(0 0,577px 0,617px 50%,577px 100%,0 100%)}
  .q2{top:292px;width:572px;clip-path:polygon(0 0,532px 0,572px 50%,532px 100%,0 100%)}
  .q3{top:383px;width:529px;clip-path:polygon(0 0,489px 0,529px 50%,489px 100%,0 100%)}
  .intro{
    position:absolute;left:35px;top:453px;width:880px;
    font-weight:700;font-size:17.5px;line-height:1.45;color:var(--ink);white-space:nowrap;
  }
  .section-title{
    position:absolute;left:0;right:0;top:510px;text-align:center;
    font-weight:700;font-size:38px;line-height:1.2;color:var(--green-title);
  }
  .benefits{
    position:absolute;left:28px;top:563px;width:877px;border-collapse:collapse;table-layout:fixed;
    border:3px solid #fff;
  }
  .benefits th,.benefits td{border:3px solid #fff;text-align:center;color:#fff;vertical-align:middle}
  .benefits th{
    height:54px;font-size:27px;font-weight:700;
    background:linear-gradient(180deg,#1d4ea4 0%,var(--navy) 50%,var(--navy-deep) 100%);
  }
  .benefits td{
    height:60px;font-size:17px;font-weight:700;line-height:1.2;
    background:linear-gradient(180deg,#4680cc 0%,var(--cell-blue) 100%);
  }
  .about-panel{position:absolute;left:0;top:822px;width:560px;height:378px}
  .about-title{
    position:absolute;left:34px;top:832px;
    font-weight:900;font-size:68px;line-height:1.2;color:#eef0ee;letter-spacing:-1px;
    text-shadow:2px 3px 4px rgba(0,0,0,.45);
  }
  .about-copy{
    position:absolute;left:35px;top:924px;width:470px;white-space:nowrap;
    font-family:"Pathway Gothic One","Arial Narrow",sans-serif;font-size:25px;line-height:32px;color:#0f2a12;
  }
  .contact-pitch{
    position:absolute;right:26px;top:826px;text-align:right;white-space:nowrap;
    font-family:"Pathway Gothic One","Arial Narrow",sans-serif;font-size:29px;line-height:35px;color:#111;
  }
  .contact-list{list-style:none}
  .contact-list li{
    position:absolute;right:38px;display:flex;justify-content:flex-end;align-items:center;gap:16px;
    font-family:"Pathway Gothic One","Arial Narrow",sans-serif;color:var(--brand-blue);
    font-size:29px;line-height:1;white-space:nowrap;
  }
  .contact-list li.phone{top:1000px}
  .contact-list li.mail{top:1053px}
  .contact-list li.web{top:1102px;font-size:37px}
  .contact-list svg{flex:none}
</style>
</head>
<body>
<main class="flier">
  <div class="hero-photo" role="img" aria-label="Smiling pharmacist in a white coat with arms crossed, standing in front of stocked pharmacy shelves"></div>
  <svg class="hero-edge" viewBox="0 0 932 460" aria-hidden="true">
    <line x1="490" y1="-4" x2="150" y2="445" stroke="var(--brand-blue)" stroke-width="7"/>
    <line x1="150" y1="444" x2="932" y2="444" stroke="var(--brand-blue)" stroke-width="4"/>
  </svg>

  <div class="brand"><span class="brand-name">Hearthway</span><span class="brand-dot"></span></div>

  <p class="question q1">Have you ever wanted to increase your marketing presence<br>and prescription volume?</p>
  <p class="question q2">Have you ever wanted to compete with the large<br>pharmacy chains?</p>
  <p class="question q3">Have you ever been frustrated by mail order<br>pharmacies taking your prescriptions?</p>

  <p class="intro">Hearthway is focused on the growth and development of local pharmacies.&nbsp; We provide your pharmacy<br>with tools to increase your efficiencies, your profits, and your ability to deliver superior patient care.</p>

  <h2 class="section-title">How do we do it?</h2>

  <table class="benefits">
    <thead>
      <tr><th>Efficiencies</th><th>Profits</th><th>Patient Care</th></tr>
    </thead>
    <tbody>
      <tr><td>No data entry</td><td>Script volume</td><td>Local pharmacy</td></tr>
      <tr><td>No third party billing</td><td>Marketing on your behalf</td><td>Positive impact to current clients</td></tr>
      <tr><td>No phone calls</td><td>Delivery<br>(use with existing clients)</td><td>Fast – same day delivery</td></tr>
    </tbody>
  </table>

  <svg class="about-panel" viewBox="0 0 560 378" aria-hidden="true">
    <defs>
      <linearGradient id="aboutGreen" x1="0" y1="0" x2="0" y2="1">
        <stop offset="0" stop-color="#3fb949"/>
        <stop offset="1" stop-color="#2ed23b"/>
      </linearGradient>
    </defs>
    <polygon points="0,4 386,4 553,210 380,378 0,378" fill="url(#aboutGreen)"/>
    <polyline points="386,4 553,210 380,378" fill="none" stroke="var(--brand-blue)" stroke-width="6"/>
  </svg>
  <h2 class="about-title">About us</h2>
  <p class="about-copy">Our solutions enable your independent pharmacy to<br>expand your prescription volume and bottom line.&nbsp; By<br>bridging the gap between pharmacies and providers, we<br>enable you to provide the superior service that local<br>pharmacies strive for.&nbsp; We believe that level of service<br>can only be provided by local pharmacies, not by<br>national chains or mail order facilities.</p>

  <p class="contact-pitch">Contact us today to learn how your pharmacy can<br>be part of a revolutionary team, one that<br>includes your pharmacy, your patients, and<br>medical professionals in your area.</p>

  <ul class="contact-list">
    <li class="phone">
      <svg width="20" height="26" viewBox="0 0 20 26" aria-hidden="true"><rect x="1" y="1" width="18" height="24" rx="3" fill="var(--green)"/><rect x="4" y="4" width="12" height="7" fill="#fff"/><g fill="#fff"><rect x="4" y="14" width="3" height="3"/><rect x="8.5" y="14" width="3" height="3"/><rect x="13" y="14" width="3" height="3"/><rect x="4" y="19" width="3" height="3"/><rect x="8.5" y="19" width="3" height="3"/><rect x="13" y="19" width="3" height="3"/></g></svg>
      <span>800-555-0142</span>
    </li>
    <li class="mail">
      <svg width="26" height="18" viewBox="0 0 26 18" aria-hidden="true"><rect x="1" y="1" width="24" height="16" fill="none" stroke="var(--green)" stroke-width="2"/><polyline points="1,1 13,10 25,1" fill="none" stroke="var(--green)" stroke-width="2"/></svg>
      <span>info@hearthway.com</span>
    </li>
    <li class="web">
      <svg width="30" height="30" viewBox="0 0 28 28" aria-hidden="true"><circle cx="14" cy="14" r="12" fill="var(--green)"/><g fill="none" stroke="#fff" stroke-width="1.6"><ellipse cx="14" cy="14" rx="5" ry="12"/><line x1="2" y1="14" x2="26" y2="14"/><line x1="4" y1="8" x2="24" y2="8"/><line x1="4" y1="20" x2="24" y2="20"/></g></svg>
      <span>www.hearthway.com</span>
    </li>
  </ul>
</main>
</body>
</html>
```